Graphic Design Banners for my newsletters: Thermomugs

We sell merchandise to business costumers. We will send newsletters every week, and I need to find someone who can make me nice banners to my newsletters.The goal with my newsletters is to SELL the products and introduce costumers to my website: www.fernvalegoods.dk. I need 3 banners to my newsletters about thermomugs:* Banner 1 - Model 37250. I think an orange round price splash (69,- v/100 stk) with this text: "Drypfri og dobbeltvægget Termokrus i rustfri stål ude og PP inde med push funktion i lækkert design."* Banner 2 - Model 82713. I think an orange round price splash (49,- v/100 stk) with this text: "Dobbeltvægget Termokrus i PP plastik i 4 forskellige farver."* Banner 3 - KT3176. Bubble price splash (45,- v/100 stk) and this text: "Dobbeltvægget termokrus med hank. Rustfri stål ude og PP inde."Maybe it will be nice if it has a "call to action" BESTIL HER (in English, it means ORDER HERE) on each banner. Here, I've attached pictures for all 3 thermomugs. The filename is the modelnumber and I sent you pictures of how it appears right now in our newsletters, and I need you to make them nicer. Personally, I like the "R&J better than the other we made." but I need help, since it looks bad and unprofessional.Thank you.

Target Market(s)

Big and middle Big companies.

Industry/Entity Type

Promotional Merchandise

Colors
faa54b

Requirements
Must have
• I sent the newletters to marketing bosses so they like Nice style and proffesionalisme. They buy my products with there logo printed on. So the product details (Nice pictures) is importent to be in focus.
Nice to have
• I have sent some banners i use on my website. I like that style. But This to newletters Could be more kvadrat.

```html
<!DOCTYPE html>
<html lang="da">
<head>
<meta charset="utf-8">
<title>Termokrus med hank – nyhedsbrev banner</title>
<link rel="stylesheet" href="https://fonts.googleapis.com/css2?family=Roboto+Condensed:wght@400;700&display=swap">
<style>
  :root {
    --paper: #ffffff;
    --ink: #1a1a1a;
    --frame: #222222;
    --orange: #f7941e;
    --orange-light: #faa54b;
    --mug-blue: #1f6fb0;
    --mug-blue-light: #5aa6dc;
    --mug-silver: #b9bbbd;
    --mug-silver-light: #eceded;
    --mug-black: #111111;
    --mug-black-light: #4a4a4a;
  }
  * { margin: 0; padding: 0; box-sizing: border-box; }
  html, body {
    width: 1200px;
    height: 600px;
    overflow: hidden;
    background: var(--paper);
  }
  .banner {
    position: relative;
    width: 1200px;
    height: 600px;
    background: var(--paper);
    font-family: "Roboto Condensed", "Arial Narrow", sans-serif;
    color: var(--ink);
    overflow: hidden;
  }
  .banner__frame {
    position: absolute;
    left: 32px;
    top: 22px;
    width: 1138px;
    height: 556px;
    border: 3px solid var(--frame);
  }
  .product-photo {
    position: absolute;
    border-radius: 14px 14px 22px 22px;
  }
  .product-photo--blue {
    left: 56px; top: 114px; width: 202px; height: 288px;
    background: linear-gradient(100deg, var(--mug-blue) 20%, var(--mug-blue-light) 55%, var(--mug-blue) 90%);
  }
  .product-photo--silver {
    left: 274px; top: 86px; width: 190px; height: 296px;
    background: linear-gradient(100deg, var(--mug-silver) 15%, var(--mug-silver-light) 50%, var(--mug-silver) 90%);
  }
  .product-photo--black {
    left: 518px; top: 120px; width: 192px; height: 302px;
    background: linear-gradient(100deg, var(--mug-black) 25%, var(--mug-black-light) 55%, var(--mug-black) 90%);
  }
  .description {
    position: absolute;
    left: 84px;
    top: 446px;
    font-size: 29px;
    font-weight: 400;
    line-height: 37px;
    color: var(--ink);
  }
  .price-splash,
  .price-splash__text {
    position: absolute;
    left: 770px;
    top: 78px;
    width: 320px;
    height: 320px;
  }
  .price-splash__text {
    display: flex;
    flex-direction: column;
    align-items: center;
    justify-content: center;
    color: var(--paper);
    transform: rotate(-14deg);
  }
  .price-splash__amount {
    font-size: 116px;
    font-weight: 700;
    line-height: 1;
    letter-spacing: 1px;
  }
  .price-splash__unit {
    font-size: 38px;
    font-weight: 400;
    line-height: 1.1;
    margin-top: 2px;
  }
  .cta {
    position: absolute;
    left: 644px;
    top: 490px;
    width: 526px;
    height: 86px;
  }
  .cta__label {
    position: absolute;
    left: 714px;
    top: 490px;
    width: 456px;
    height: 86px;
    display: flex;
    align-items: center;
    justify-content: center;
    font-size: 29px;
    font-weight: 700;
    color: var(--ink);
    text-decoration: none;
    letter-spacing: 0.3px;
  }
</style>
</head>
<body>
  <main class="banner">
    <div class="banner__frame"></div>

    <div class="product-photo product-photo--blue" role="img" aria-label="Blåt termokrus i rustfrit stål med sort hank og låg"></div>
    <div class="product-photo product-photo--silver" role="img" aria-label="Sølvfarvet termokrus i rustfrit stål med sort hank og låg"></div>
    <div class="product-photo product-photo--black" role="img" aria-label="Sort termokrus med sort hank og låg"></div>

    <p class="description">
      Dobbeltvægget termokrus med hank.<br>
      Rustfri stål ude og PP inde.
    </p>

    <svg class="price-splash" viewBox="0 0 320 320" aria-hidden="true">
      <circle cx="160" cy="160" r="155" fill="var(--orange)"/>
    </svg>
    <div class="price-splash__text">
      <span class="price-splash__amount">45,-</span>
      <span class="price-splash__unit">v/100 stk</span>
    </div>

    <svg class="cta" viewBox="0 0 526 86" aria-hidden="true">
      <polygon points="82,0 526,0 526,86 0,86" fill="var(--orange)"/>
    </svg>
    <a class="cta__label" href="#">BESTIL OG SE MERE HER</a>
  </main>
</body>
</html>
```